Business Card Design Project

Refresh of logo attached. Require text underneath to be more ledgible, crisper & cleaner.

Overall, staying with same colour scheme need a brighter, crisper, easily readible business card style.

Industry/Entity Type

Business

```html
<!DOCTYPE html>
<html lang="en">
<head>
<meta charset="utf-8">
<title>Northbridge Institute of Estate Advisors — Business Card</title>
<link rel="stylesheet" href="https://fonts.googleapis.com/css2?family=Arimo:wght@400;700&display=swap">
<style>
  :root {
    --backdrop: #e9ebec;
    --card: #fbfbfa;
    --ink-grey: #5f6266;
    --ink-dark-teal: #34596a;
    --ink-teal: #3a85a3;
    --rule-brown: #6b5650;
    --shadow: rgba(40, 50, 60, 0.18);
  }
  * { box-sizing: border-box; margin: 0; padding: 0; }
  html, body {
    width: 1200px; height: 800px; overflow: hidden;
    background: var(--backdrop);
    font-family: "Arimo", Arial, sans-serif;
  }
  .canvas {
    width: 1200px; height: 800px;
    display: flex; align-items: center; justify-content: center; gap: 44px;
  }
  .card {
    position: relative;
    width: 520px; height: 300px;
    background: var(--card);
    box-shadow: 0 10px 28px var(--shadow);
    overflow: hidden;
  }

  /* Front */
  .card--front { display: flex; align-items: center; justify-content: center; }
  .lockup { display: flex; flex-direction: column; align-items: flex-start; }
  .lockup__name { display: flex; align-items: center; gap: 14px; }
  .lockup__square { width: 36px; height: 36px; background: var(--ink-teal); }
  .lockup__wordmark {
    font-size: 54px; font-weight: 400; letter-spacing: 3px;
    color: var(--ink-grey); line-height: 1;
  }
  .lockup__rule { width: 270px; height: 1.5px; background: var(--rule-brown); margin: 10px 0 6px; }
  .lockup__descriptor {
    font-size: 11px; letter-spacing: 2.4px; line-height: 1.3;
    color: var(--ink-grey); text-transform: uppercase;
  }

  /* Back */
  .card--back .mark-area {
    position: absolute; left: 0; top: 0; width: 290px; height: 100%;
    display: flex; align-items: center; justify-content: center;
  }
  .mark-area__wordmark { font-size: 64px; letter-spacing: 4px; color: var(--ink-dark-teal); }
  .card--back .divider {
    position: absolute; left: 296px; top: 40px; width: 2px; height: 220px;
    background: var(--ink-dark-teal);
  }
  .card--back .edge-band {
    position: absolute; left: 0; bottom: 0; width: 290px; height: 8px;
    background: var(--ink-dark-teal);
  }
  .contact {
    position: absolute; left: 298px; right: 0; top: 36px;
    display: flex; flex-direction: column; align-items: center; text-align: center;
  }
  .contact__name { font-size: 21px; font-weight: 700; color: var(--ink-dark-teal); letter-spacing: -0.5px; }
  .contact__title { font-size: 12px; color: var(--ink-teal); margin-top: 2px; }
  .contact__icon { width: 16px; height: 16px; margin: 14px 0 6px; }
  .contact__line { font-size: 12.5px; color: var(--ink-grey); line-height: 1.45; }
</style>
</head>
<body>
<main class="canvas">

  <section class="card card--back" aria-label="Card back">
    <div class="mark-area">
      <span class="mark-area__wordmark">NIEA</span>
    </div>
    <div class="edge-band"></div>
    <div class="divider"></div>
    <div class="contact">
      <p class="contact__name">Daniel R. Hartley</p>
      <p class="contact__title">Certified Executor Advisor</p>

      <svg class="contact__icon" viewBox="0 0 16 16" aria-hidden="true">
        <rect x="4" y="1" width="8" height="14" rx="1.5" fill="none" stroke="#34596a" stroke-width="1.4"/>
        <line x1="7" y1="12.5" x2="9" y2="12.5" stroke="#34596a" stroke-width="1.4"/>
      </svg>
      <p class="contact__line">(416) 555 0142</p>
      <p class="contact__line">(647) 555 0187</p>

      <svg class="contact__icon" viewBox="0 0 16 16" aria-hidden="true">
        <rect x="1" y="3" width="14" height="10" fill="#34596a"/>
        <polyline points="1,3 8,9 15,3" fill="none" stroke="#fbfbfa" stroke-width="1.2"/>
      </svg>
      <p class="contact__line">daniel@niea.ca</p>

      <svg class="contact__icon" viewBox="0 0 16 16" aria-hidden="true">
        <rect x="1.5" y="2" width="13" height="9" fill="none" stroke="#34596a" stroke-width="1.4"/>
        <line x1="5" y1="14" x2="11" y2="14" stroke="#34596a" stroke-width="1.4"/>
      </svg>
      <p class="contact__line">www.niea.ca</p>
    </div>
  </section>

  <section class="card card--front" aria-label="Card front">
    <div class="lockup">
      <div class="lockup__name">
        <span class="lockup__square"></span>
        <span class="lockup__wordmark">NIEA</span>
      </div>
      <div class="lockup__rule"></div>
      <p class="lockup__descriptor">Northbridge Institute of<br>Estate Advisors</p>
    </div>
  </section>

</main>
</body>
</html>
```